B2B telecom company need web design

We need a web design for our corporate web site. The company exists since almost 10 years.
This is a DESIGN contest, you're expected to provide design only, NOT the whole website. The winner will have to provide the HTML template (with Lorem Ipsum content) and the CSS files of his design.
Our initial product is SMS peering in P2P (you send a SMS to a friend in a foreign country, great chance that your operator route your SMS to us that we route to the recipient). We're launching a bulk SMS service (marketing and application to SMS).
Target is mostly corporate, usually big corporate (operators, contents providers...) where use of SMS is part of the main business.
The web site is composed of 1 landing page and 7 content pages (plan is given for your information, all content page are using the same template and the same design, you do NOT need to make one design per page) :
* About US
Company Profile
They trust us
The Volnor Team
Partners
Contact us
* Solution
P2P SMS
A2P SMS
You only need to submit the landing page and a template page for the content (with h1, h2, h3 and h4).
Design must be based on our new logo (see attached file).
Our current web site http://www.volnor-example.com
The winner of the contest will have to provide state of the art HTML template and CSS files of his design. Photo used shall be downloaded from Pixelbrook (provide the ID of the picture that we purchase file).
Target Market(s)
Telecom operator. SMS Peering hubs. Bulk SMS.
Industry/Entity Type
It Company
Number of Pages Required
2 page

```html
<!DOCTYPE html>
<html lang="en">
<head>
<meta charset="utf-8">
<title>Volnor Mobile</title>
<link href="https://fonts.googleapis.com/css2?family=Open+Sans:wght@400;600;700&display=swap" rel="stylesheet">
<style>
  :root {
    --canvas: #efefef;
    --page-soft: #f7f7f7;
    --white: #ffffff;
    --green: #86c229;
    --ink: #1c1c1c;
    --grey-text: #5e5e5e;
    --body-text: #777777;
    --hero-deep: #050a2a;
    --hero-mid: #123a86;
    --hero-light: #3f9ad6;
  }
  * { box-sizing: border-box; margin: 0; padding: 0; }
  html, body { width: 1200px; height: 1200px; overflow: hidden; }
  body {
    background: var(--canvas);
    font-family: "Open Sans", Arial, sans-serif;
    position: relative;
  }
  .page {
    position: absolute;
    left: 130px; top: 0;
    width: 939px; height: 1200px;
    background: var(--page-soft);
    box-shadow: 0 0 24px rgba(0,0,0,0.12);
    overflow: hidden;
  }
  .hero {
    position: absolute; left: 0; top: 0;
    width: 939px; height: 503px;
    background:
      radial-gradient(ellipse 55% 45% at 52% 42%, var(--hero-light) 0%, var(--hero-mid) 45%, transparent 80%),
      radial-gradient(ellipse 80% 70% at 50% 45%, #0e2c6e 0%, var(--hero-deep) 85%);
    text-align: center;
    color: var(--white);
  }
  .site-name {
    position: absolute; left: 36px; top: -12px;
    font-size: 20px; font-weight: 400; color: var(--white);
  }
  .main-nav {
    position: absolute; right: 40px; top: -8px;
    display: flex; gap: 18px;
    font-size: 12px; color: var(--white);
  }
  .hero-title {
    position: absolute; left: 0; right: 0; top: 183px;
    font-size: 40px; font-weight: 700; letter-spacing: 0.3px;
  }
  .hero-tagline {
    position: absolute; left: 0; right: 0; top: 238px;
    font-size: 14px; font-weight: 400;
  }
  .feature {
    position: absolute; top: 503px;
    height: 459px; width: 458px;
    text-align: center;
  }
  .feature--about { left: 0; background: var(--white); color: var(--grey-text); }
  .feature--services { left: 481px; background: var(--green); color: var(--white); }
  .feature-title {
    position: absolute; left: 0; right: 0; top: 98px;
    font-size: 18px; font-weight: 400;
  }
  .feature-text {
    position: absolute; left: 0; right: 0; top: 200px;
    font-size: 19px; line-height: 26px;
  }
  .feature--services .feature-text { font-weight: 600; }
  .feature-button {
    position: absolute; top: 324px;
    width: 114px; height: 28px;
    font-size: 11px; line-height: 26px;
    text-transform: uppercase;
  }
  .feature--about .feature-button { left: 175px; border: 1px solid var(--grey-text); color: var(--grey-text); }
  .feature--services .feature-button { left: 171px; background: var(--white); color: var(--green); border: 1px solid var(--white); }
  .intro-brand {
    position: absolute; left: 89px; top: 1163px;
    font-size: 28px; font-weight: 400; color: var(--grey-text);
    letter-spacing: 1.6px;
    white-space: nowrap;
  }
  .intro-title {
    position: absolute; left: 377px; top: 1036px;
    font-size: 22px; font-weight: 400; color: var(--ink);
  }
  .intro-text {
    position: absolute; left: 377px; top: 1088px; width: 500px;
    font-size: 11.8px; line-height: 22.5px; color: var(--body-text);
  }
</style>
</head>
<body>
  <div class="page">
    <header class="hero" role="img" aria-label="Glowing world map with connection lines on a deep blue background">
      <div class="site-name">Volnor mobile</div>
      <nav class="main-nav"><span>About</span><span>Services</span><span>Why us</span><span>News</span><span>Contact</span></nav>
      <h1 class="hero-title">WE CONNECT YOU CREATIVELY</h1>
      <p class="hero-tagline">MARKETERS . INNOVATERS . CONSULTANTS</p>
    </header>

    <section class="feature feature--about">
      <h2 class="feature-title">WHO WE ARE</h2>
      <p class="feature-text">We are Consultants,<br>Creators and Innovators</p>
      <div class="feature-button">About us</div>
    </section>

    <section class="feature feature--services">
      <h2 class="feature-title">OUR SERVICES</h2>
      <p class="feature-text">We have won several awards &amp;<br>trust of many fortune 500</p>
      <div class="feature-button">Services</div>
    </section>

    <div class="intro-brand">Volnor mobile</div>
    <h2 class="intro-title">WE ARE VOLNOR MOBILE</h2>
    <p class="intro-text">In 2007, Kestrel 365, the global leader in mobile messaging, announced the launch of the Regional Messaging Exchange (VOLNOR Mobile Exchange) mobile messaging hub, to consolidate its position as the major provider of international SMS across Africa and the Middle East .<br>The new Hub allows to expand further into this fast-growing region and offer international</p>
  </div>
</body>
</html>
```